Redesign website for small print company

Vindaborgprent is a small printing company in Iceland mainly servicing Students, schools, etc. We are also doing all kind of other jobs, like business cards, book printing, brochure printing etc. We are also selling books online.
Our website is: www.vindaborgprent.is
What we are looking for is:
- Web Design (Uncoded - PSD layout only)
- Mobile friendly design, using our current color scheme: Red, green, yellow and light gray.
- Clean simple design
- Simple, light and easy to use.
- More menu Items/drop down
Industry/Entity Type
Digital Printing
Number of Pages Required
5+ page
Requirements
Must have
- Easy navigation
- Designed for mobile
- Current color scheme (see logo)
Nice to have
- Icon based products

```html
<!DOCTYPE html>
<html lang="is">
<head>
<meta charset="utf-8">
<title>Vindaborgprent</title>
<link rel="stylesheet" href="https://fonts.googleapis.com/css2?family=Montserrat:wght@500;600;700&family=Roboto:wght@400;500&display=swap">
<style>
:root{
  --green:#0e6b32;
  --red:#e3262b;
  --yellow:#ffe400;
  --lime:#d8f000;
  --dark:#2f2f2f;
  --ink:#111;
  --gray:#ececec;
  --white:#fff;
}
*{margin:0;padding:0;box-sizing:border-box}
html,body{width:1200px;height:2644px;overflow:hidden;background:var(--white)}
body{position:relative;font-family:"Roboto",sans-serif;color:var(--ink)}
.abs{position:absolute}
.topbar{left:406px;top:0;width:794px;height:48px;background:var(--green);border-bottom-left-radius:40px;color:var(--white);font:600 19px "Montserrat",sans-serif;display:flex;align-items:center;gap:16px;padding-left:52px}
.topbar .dot{width:28px;height:28px;border:2px solid var(--white);border-radius:50%}
.topbar .flag{width:30px;height:30px;border-radius:50%}
.brand{left:53px;top:46px;display:flex;align-items:center;gap:12px;font:700 32px "Montserrat",sans-serif;color:var(--ink)}
.brand .mark{width:44px;height:44px;background:var(--red)}
.nav{left:424px;top:72px;display:flex;gap:36px;font:600 25px "Montserrat",sans-serif}
.nav .active{border-bottom:4px solid var(--red);padding-bottom:4px}
.hero{left:0;top:127px;width:1200px;height:597px;background:linear-gradient(120deg,#f7d300 0%,#f08a1c 30%,#e5342d 55%,#c23aa6 75%,#3a7bd8 100%)}
.hero h1{position:absolute;left:53px;top:72px;font:700 80px/1.22 "Montserrat",sans-serif;color:var(--ink)}
.hero h2{position:absolute;left:53px;top:340px;font:600 58px/1.2 "Montserrat",sans-serif;color:var(--ink)}
.hero .people{position:absolute;left:640px;top:150px;width:520px;height:447px;background:linear-gradient(180deg,rgba(240,220,200,.5),rgba(120,90,110,.6));border-radius:10px 10px 0 0}
.section-title{font:500 33px "Montserrat",sans-serif;color:var(--ink)}
.section-title::after{content:"";display:block;width:66px;height:4px;background:var(--red);margin-top:10px}
.pill{background:var(--yellow);font:600 32px "Montserrat",sans-serif;display:flex;align-items:center;justify-content:center;border-radius:46px 0 0 46px}
.pill.round{border-radius:46px}
.step{font:500 28px "Montserrat",sans-serif}
.tile{overflow:hidden}
.tile .photo{position:absolute;inset:0;background:linear-gradient(160deg,#f4f4f4,#cfcfcf)}
.tile span{position:absolute;left:0;right:0;bottom:10px;text-align:center;font:700 52px "Montserrat",sans-serif;color:var(--ink)}
.about p{font:400 24px/34px "Roboto",sans-serif}
.footer{left:0;top:2344px;width:1200px;height:300px;background:var(--gray)}
.footer .col{position:absolute;top:18px;font:400 28px/40px "Roboto",sans-serif}
.footer h4{font:600 28px "Montserrat",sans-serif;line-height:34px}
.card{width:130px;height:60px;border-radius:10px;background:#777;color:var(--white);font:600 16px "Montserrat",sans-serif;display:flex;align-items:center;justify-content:center}
</style>
</head>
<body>

<div class="abs topbar">
  <span>Follow us</span><span class="dot"></span><span class="dot"></span><span class="dot"></span>
  <svg width="26" height="30" viewBox="0 0 24 24"><path fill="#fff" d="M6.6 10.8a15 15 0 0 0 6.6 6.6l2.2-2.2a1 1 0 0 1 1-.25 11 11 0 0 0 3.6.6 1 1 0 0 1 1 1V20a1 1 0 0 1-1 1A17 17 0 0 1 3 4a1 1 0 0 1 1-1h3.5a1 1 0 0 1 1 1c0 1.25.2 2.45.6 3.6a1 1 0 0 1-.25 1z"/></svg>
  <span>555 0142</span>
  <span style="margin-left:24px">Mon - Fri: 9-17</span>
  <span class="flag" style="background:#2a3d8f;margin-left:28px"></span><span class="flag" style="background:#1f4fa8"></span>
</div>

<div class="abs brand"><span class="mark"></span>VINDABORGPRENT</div>

<nav class="abs nav">
  <span class="active">Heim</span><span>Þjónusta</span><span>Skil á verkum</span><span>Um okkur</span>
</nav>
<svg class="abs" style="left:1058px;top:72px" width="34" height="34" viewBox="0 0 24 24"><circle cx="10" cy="10" r="7" fill="none" stroke="#111" stroke-width="2.4"/><path d="M15 15l6 6" stroke="#111" stroke-width="2.6"/></svg>
<svg class="abs" style="left:1122px;top:70px" width="30" height="36" viewBox="0 0 20 24"><rect x="2" y="7" width="16" height="15" rx="1.5" fill="none" stroke="#111" stroke-width="2.2"/><path d="M6 9V5a4 4 0 0 1 8 0v4" fill="none" stroke="#111" stroke-width="2.2"/></svg>

<section class="abs hero">
  <h1>Engar áhyggjur<br>...Þetta reddast</h1>
  <h2>Við prentum<br>ritgerðir,skýslur...</h2>
  <div class="people" role="img" aria-label="Þrír brosandi nemendur gefa þumalinn upp"></div>
</section>

<div class="abs section-title" style="left:58px;top:776px">Hvernig það virkar?</div>
<div class="abs pill" style="left:896px;top:776px;width:304px;height:92px">Skil á verkum</div>

<div class="abs step" style="left:70px;top:850px">Senda verk</div>
<div class="abs step" style="left:392px;top:850px">Hanna verk</div>
<div class="abs step" style="left:742px;top:850px">Fá Tilboð</div>

<svg class="abs" style="left:58px;top:893px" width="940" height="162" viewBox="0 0 940 162">
  <g>
    <polygon points="0,40 30,80 0,120 20,120 50,80 20,40" fill="var(--lime)"/>
    <polygon points="12,0 170,0 236,81 170,162 12,162 60,81" fill="var(--dark)"/>
    <polyline points="170,0 236,81 170,162" fill="none" stroke="var(--red)" stroke-width="4"/>
    <path d="M60 130 C70 80 110 60 150 60 L150 38 L200 80 L150 122 L150 98 C110 98 80 110 60 130Z" fill="#eee"/>
  </g>
  <g transform="translate(322,0)">
    <polygon points="0,40 30,80 0,120 20,120 50,80 20,40" fill="var(--lime)"/>
    <polygon points="12,0 194,0 260,81 194,162 12,162 60,81" fill="var(--dark)"/>
    <polyline points="194,0 260,81 194,162" fill="none" stroke="var(--green)" stroke-width="4"/>
    <ellipse cx="140" cy="82" rx="58" ry="50" fill="#eee"/>
    <circle cx="115" cy="60" r="9" fill="var(--dark)"/><circle cx="145" cy="50" r="9" fill="var(--dark)"/><circle cx="172" cy="68" r="9" fill="var(--dark)"/><circle cx="112" cy="95" r="9" fill="var(--dark)"/><circle cx="160" cy="108" r="13" fill="var(--dark)"/>
  </g>
  <g transform="translate(676,0)">
    <polygon points="0,40 30,80 0,120 20,120 50,80 20,40" fill="var(--lime)"/>
    <polygon points="12,0 180,0 246,81 180,162 12,162 60,81" fill="var(--dark)"/>
    <polyline points="180,0 246,81 180,162" fill="none" stroke="var(--red)" stroke-width="4"/>
    <g fill="none" stroke="#eee" stroke-width="4">
      <circle cx="85" cy="42" r="12"/><circle cx="128" cy="60" r="12"/><circle cx="170" cy="42" r="12"/>
      <path d="M70 130 L100 108 L140 108 M70 130 L150 130 L185 100"/>
    </g>
  </g>
</svg>

<div class="abs section-title" style="left:50px;top:1106px">VÖRUFLOKKAR</div>

<div class="abs tile" style="left:0;top:1186px;width:399px;height:323px"><div class="photo" role="img" aria-label="Nafnspjöld í stafla"></div><span>Nafnspjöld</span></div>
<div class="abs tile" style="left:408px;top:1186px;width:386px;height:323px"><div class="photo" role="img" aria-label="Opnir bæklingar á borði"></div><span>Bæklingar</span></div>
<div class="abs tile" style="left:803px;top:1186px;width:397px;height:323px"><div class="photo" role="img" aria-label="Innbundin ritgerð"></div><span>Ritgerðir</span></div>
<div class="abs tile" style="left:0;top:1536px;width:399px;height:326px"><div class="photo" role="img" aria-label="Kennslubækur á borði"></div><span>Kennslubækur</span></div>
<div class="abs tile" style="left:408px;top:1536px;width:386px;height:326px"><div class="photo" role="img" aria-label="Prentaðar bækur í hrúgu"></div><span>Bókaprentun</span></div>
<div class="abs tile" style="left:803px;top:1536px;width:397px;height:326px"><div class="photo" role="img" aria-label="Upprúlluð veggspjöld"></div><span>Veggspjöld</span></div>

<div class="abs section-title" style="left:80px;top:1929px">UM OKKUR</div>
<div class="abs pill round" style="left:888px;top:1915px;width:289px;height:97px">Lestu meira</div>

<div class="abs" style="left:49px;top:2003px;width:203px;height:262px;background:var(--red)"></div>
<div class="abs about" style="left:296px;top:2018px;width:870px">
  <p>Velkomin í Vindaborgprent<br>Vindaborgprent er fyrirtæki staðsett á háskólasvæðinu sem hefur sérhæft sig í að þjónusta skólafólk, ásamt því að sinna allri almennri prentun fyrir almenning.</p>
  <p style="margin-top:34px">Vindaborgprent gefur út greinasöfn og frumsamdar kennslubækur fyrir námskeið...</p>
</div>

<footer class="abs footer">
  <div class="col" style="left:58px">Heim<br>Þjónusta<br>Skil á verkum<br>Um okkur</div>
  <div class="col" style="left:357px"><h4>VÖRUFLOKKAR</h4>Nafnspjöld<br>Bæklingar<br>Ritgerðir<br>Kennslubækur<br>Bókaprentun<br>Veggspjöld</div>
  <div class="col" style="left:692px">
    <h4>Follow us</h4>
    <div style="display:flex;gap:8px;margin-top:8px"><span style="width:34px;height:34px;border:2px solid #111;border-radius:50%"></span><span style="width:34px;height:34px;border:2px solid #111;border-radius:50%"></span><span style="width:34px;height:34px;border:2px solid #111;border-radius:50%"></span></div>
    <div style="display:flex;align-items:center;gap:8px;font:500 19px Roboto,sans-serif;margin-top:10px">
      <svg width="24" height="26" viewBox="0 0 24 24"><path fill="#111" d="M6.6 10.8a15 15 0 0 0 6.6 6.6l2.2-2.2a1 1 0 0 1 1-.25 11 11 0 0 0 3.6.6 1 1 0 0 1 1 1V20a1 1 0 0 1-1 1A17 17 0 0 1 3 4a1 1 0 0 1 1-1h3.5a1 1 0 0 1 1 1c0 1.25.2 2.45.6 3.6a1 1 0 0 1-.25 1z"/></svg>555 0142</div>
    <div style="font:400 19px Roboto,sans-serif;margin-top:10px;padding-left:50px">Mon - Fri: 9-17</div>
  </div>
  <div class="abs card" style="left:1000px;top:22px">Kortagreiðsla</div>
  <div class="abs card" style="left:1000px;top:100px">Greiðslukort</div>
  <div class="abs" style="left:756px;top:220px;font:600 29px Roboto,sans-serif">© 2018, Vindaborgprent</div>
</footer>

</body>
</html>
```